STOREFRONT LIT SIGN for The Cantera Loft

A sign advertising our music academy. This sign will be hung 10 feet above the entrance of our building and will be seen by all pedestrian and vehicle traffic on Main Street Delano.

Target Market(s)

Street passerby

Industry/Entity Type

Music Training

Font styles to use
Other font styles liked:
• Creative

Colors

Designer to choose colors to be used in the design.

Requirements
Must have
• A White Background
• Dimensions: 8 ft long x 3 ft tall
• The Cantera Loft of Delano
• Lecciones de Piano, Violin, Guitarra, Voz, Trompeta y Mas
• MUSIC ACADEMY *(This should be most prominent)
• Guitar, Voice, Trumpet and More
• (661) 478-5926
• thecanteraloft.example
Nice to have
• Graphics of a piano, or guitar, or violin or trumpet or a combination of two or more

```html
<!DOCTYPE html>
<html lang="en">
<head>
<meta charset="utf-8">
<title>The Cantera Loft of Delano – Storefront Sign</title>
<link href="https://fonts.googleapis.com/css2?family=Kaushan+Script&family=Montserrat:wght@700;800&display=swap" rel="stylesheet">
<style>
  :root {
    --stage: #eceef0;
    --sign-white: #ffffff;
    --sign-mist: #e3e7eb;
    --academy-red: #c8101a;
    --name-blue: #174a94;
    --name-blue-deep: #0f3470;
    --ink: #111111;
    --contact-gray: #3a3a3a;
    --art-light: #eef0f2;
    --art-mid: #c9cdd2;
    --art-dark: #5a5e63;
  }
  * { margin: 0; padding: 0; box-sizing: border-box; }
  html, body {
    width: 1200px; height: 581px; overflow: hidden;
    background: var(--stage);
  }
  .sign {
    position: absolute; left: 0; top: 65px;
    width: 1200px; height: 450px; overflow: hidden;
    background:
      linear-gradient(165deg, transparent 40%, rgba(210,215,220,.45) 55%, transparent 70%),
      linear-gradient(180deg, var(--sign-white) 0%, var(--sign-mist) 55%, var(--sign-white) 100%);
    font-family: "Montserrat", Arial, sans-serif;
  }
  .violin-art {
    position: absolute; left: 0; top: 8px; width: 144px; height: 442px;
    background: radial-gradient(ellipse at 50% 70%, var(--art-mid) 0%, var(--art-light) 65%, transparent 75%);
  }
  .clef-art {
    position: absolute; right: 0; top: 12px; width: 177px; height: 438px;
    background: radial-gradient(ellipse at 50% 50%, var(--art-dark) 0%, var(--art-mid) 45%, transparent 72%);
    opacity: .7;
  }
  .academy-title {
    position: absolute; left: 0; right: 0; top: 16px;
    text-align: center;
    font-weight: 800; font-size: 47px; letter-spacing: 20px;
    color: var(--academy-red);
    padding-left: 20px;
  }
  .studio-name {
    position: absolute; left: 0; right: 0; top: 78px;
    text-align: center;
    font-family: "Kaushan Script", "Brush Script MT", cursive;
    font-size: 80px; line-height: 74px;
    color: var(--name-blue);
  }
  .lessons-es {
    position: absolute; left: 0; right: 0; top: 285px;
    text-align: center;
    font-weight: 700; font-size: 21px;
    color: var(--ink);
  }
  .lessons-en {
    position: absolute; left: 0; right: 0; top: 332px;
    text-align: center;
    font-weight: 800; font-size: 35px;
    color: var(--academy-red);
  }
  .divider {
    position: absolute; left: 525px; top: 385px;
    width: 150px; height: 2px; background: var(--academy-red);
  }
  .contact {
    position: absolute; left: 0; right: 0; top: 398px;
    display: flex; justify-content: center; align-items: center; gap: 14px;
    font-weight: 700; font-size: 29px;
    color: var(--contact-gray);
  }
  .contact-item { display: flex; align-items: center; gap: 14px; }
  .contact-icon { width: 26px; height: 26px; flex: none; }
</style>
</head>
<body>
  <main class="sign">
    <div class="violin-art" role="img" aria-label="Violin silhouette built from scattered music notes"></div>
    <div class="clef-art" role="img" aria-label="Large treble clef formed by piano keys"></div>

    <h1 class="academy-title">MUSIC ACADEMY</h1>
    <p class="studio-name">The Cantera Loft<br>of Delano</p>

    <p class="lessons-es">LECCIONES DE PIANO, VIOLIN, GUITARRA, VOZ, TROMPETA Y MAS</p>
    <p class="lessons-en">GUITAR, VOICE, TRUMPET AND MORE</p>
    <div class="divider"></div>

    <div class="contact">
      <span class="contact-item">
        <svg class="contact-icon" viewBox="0 0 26 26" aria-hidden="true">
          <circle cx="13" cy="13" r="13" fill="var(--academy-red)"/>
          <path d="M9 7.5c.8-.6 1.6-.4 2 .3l1.1 2c.3.6.1 1.2-.4 1.6l-.8.6c.6 1.5 1.7 2.7 3.2 3.4l.6-.8c.4-.5 1-.7 1.6-.4l2 1.1c.7.4.9 1.2.3 2-1.2 1.6-3 1.9-5 .7-2.6-1.5-4.4-3.6-5.4-6.3-.6-1.7-.3-3.2.8-4.2z" fill="#fff"/>
        </svg>
        (661) 478-5926
      </span>
      <span class="contact-item">
        <svg class="contact-icon" viewBox="0 0 26 26" aria-hidden="true">
          <g fill="none" stroke="var(--academy-red)" stroke-width="2">
            <circle cx="13" cy="13" r="11.5"/>
            <ellipse cx="13" cy="13" rx="5" ry="11.5"/>
            <line x1="1.5" y1="13" x2="24.5" y2="13"/>
            <path d="M3.5 7h19M3.5 19h19"/>
          </g>
        </svg>
        WWW.THECANTERALOFT.EXAMPLE
      </span>
    </div>
  </main>
</body>
</html>
```